New business card for a regional office of a US M&A company

We need business card for a finance company, office based in Hong Kong , our Head office is in US, our business is to Merge and acquires companies , the new office will be a regional office for the Asia Pacific region. We want to use the head office logo as attached ( but don't have to be exactly the same, can be a variation to it) as a base and then add Asia Pacific alongside the logo.
We would prefer to have be bilingual Eng + Chinese, although we don't really have Chinese company name .

Industry/Entity Type

Business

Contact Information for Business Card

Carla Beth Soren
 

VP,
APAC M&A Operations
Tovar Crest Asia Pacific Limited
 
Unit 1407, K82
27 Sai Lok Fung Road, 
Hong Kong 
 
M: +852 6481 2037
T : +852 2736 4100
F : +852 2736 4155
VOIP: 4813
 
cbsoren@tovarcrest.com

Font styles to use
Serif
Sans Serif

Colors

Designer to choose colors to be used in the design.

Requirements
Must have
• APAC Office

```html
<!DOCTYPE html>
<html lang="en">
<head>
<meta charset="utf-8">
<title>Tovar Crest Asia Pacific – Business Card</title>
<link href="https://fonts.googleapis.com/css2?family=Open+Sans:wght@400;600;700;800&display=swap" rel="stylesheet">
<style>
  :root {
    --navy: #0f2a47;
    --navy-deep: #0a2139;
    --cyan: #1fb3cf;
    --ink: #4a4f55;
    --paper: #ffffff;
    --backdrop: #d9dbdd;
  }
  * { box-sizing: border-box; margin: 0; padding: 0; }
  html, body { width: 1200px; height: 900px; overflow: hidden; }
  body {
    background: var(--backdrop);
    font-family: "Open Sans", sans-serif;
    display: flex;
    flex-direction: column;
    align-items: center;
    justify-content: center;
    gap: 26px;
  }
  .card {
    width: 720px;
    height: 411px;
    position: relative;
    overflow: hidden;
    box-shadow: 0 8px 24px rgba(0,0,0,0.22);
  }

  /* Back face */
  .card-back {
    background: radial-gradient(ellipse at 45% 35%, #143458 0%, var(--navy-deep) 75%);
    display: flex;
    align-items: center;
    justify-content: center;
    gap: 14px;
  }
  .back-mark {
    width: 26px; height: 26px;
    background: var(--paper);
  }
  .back-name {
    color: var(--paper);
    font-weight: 800;
    font-size: 40px;
    letter-spacing: 1px;
  }

  /* Front face */
  .card-front { background: var(--paper); }
  .brand {
    position: absolute;
    left: 40px; top: 130px;
    width: 330px;
    display: flex;
    flex-direction: column;
    align-items: center;
    gap: 18px;
  }
  .brand-mark {
    width: 52px; height: 52px;
    background: var(--navy);
  }
  .brand-name {
    color: var(--cyan);
    font-weight: 800;
    font-size: 42px;
    letter-spacing: 1px;
    white-space: nowrap;
  }
  .name-bar {
    position: absolute;
    left: 392px; top: 86px;
    width: 4px; height: 42px;
    background: var(--navy);
  }
  .divider {
    position: absolute;
    left: 386px; top: 142px;
    width: 2px; height: 148px;
    background: var(--cyan);
  }
  .person {
    position: absolute;
    left: 418px; top: 82px;
  }
  .person-name {
    color: var(--cyan);
    font-weight: 600;
    font-size: 27px;
    letter-spacing: 0.5px;
    line-height: 1.1;
  }
  .person-title {
    color: var(--navy);
    font-weight: 700;
    font-size: 13.5px;
    letter-spacing: 0.6px;
    margin-top: 4px;
  }
  .contacts {
    position: absolute;
    left: 414px; top: 150px;
    list-style: none;
  }
  .contacts li {
    display: flex;
    align-items: center;
    gap: 14px;
    color: var(--ink);
    font-size: 15px;
    letter-spacing: 0.8px;
    line-height: 21px;
  }
  .contacts svg { width: 12px; height: 12px; fill: var(--cyan); flex: none; }
  .address {
    position: absolute;
    left: 412px; top: 248px;
    color: var(--ink);
    font-size: 17px;
    line-height: 25px;
    letter-spacing: 0.3px;
  }
  .wave {
    position: absolute;
    left: 0; bottom: 0;
    width: 720px; height: 96px;
  }
  .voip {
    position: absolute;
    left: 280px; bottom: 16px;
    color: var(--paper);
    font-size: 16px;
    letter-spacing: 1px;
  }
</style>
</head>
<body>

  <section class="card card-back">
    <div class="back-mark"></div>
    <div class="back-name">TOVAR CREST</div>
  </section>

  <section class="card card-front">
    <div class="brand">
      <div class="brand-mark"></div>
      <div class="brand-name">TOVAR CREST</div>
    </div>

    <div class="name-bar"></div>
    <div class="divider"></div>

    <div class="person">
      <div class="person-name">Carla Beth Soren</div>
      <div class="person-title">VP, APAC M&amp;A Operations</div>
    </div>

    <ul class="contacts">
      <li>
        <svg viewBox="0 0 12 12" aria-hidden="true"><path d="M3 0h6a1 1 0 0 1 1 1v10a1 1 0 0 1-1 1H3a1 1 0 0 1-1-1V1a1 1 0 0 1 1-1zm0 1.5v8h6v-8z"/></svg>
        +852 6481 2037
      </li>
      <li>
        <svg viewBox="0 0 12 12" aria-hidden="true"><path d="M2.5 0.5l2 2.5-1.2 1.3a7 7 0 0 0 4.4 4.4L9 7.5l2.5 2-1.3 2C5 11 1 7 0.5 1.8z"/></svg>
        +852 2736 4100
      </li>
      <li>
        <svg viewBox="0 0 12 12" aria-hidden="true"><path d="M3 0h6v3H3zM1 4h10a1 1 0 0 1 1 1v4H9.5v3h-7V9H0V5a1 1 0 0 1 1-1zm3 5v2h4V9z"/></svg>
        +852 2736 4155
      </li>
      <li>
        <svg viewBox="0 0 12 12" aria-hidden="true"><path d="M0 2h12v1L6 7 0 3zM0 4.5l6 4 6-4V10H0z"/></svg>
        cbsoren@tovarcrest.com
      </li>
    </ul>

    <div class="address">
      Unit 1407, K82 27 Sai Lok<br>
      Fung Road, Hong Kong
    </div>

    <svg class="wave" viewBox="0 0 720 96" preserveAspectRatio="none" aria-hidden="true">
      <path d="M0 0 C200 20 420 40 720 88 L720 96 L0 96 Z" fill="var(--navy)"/>
      <path d="M300 30 C460 42 600 62 720 74 L720 88 C600 70 470 50 300 30 Z" fill="var(--cyan)"/>
    </svg>
    <div class="voip">VOIP: 4813</div>
  </section>

</body>
</html>
```